A5 Flyer for Financial Services Business

I am after a re-design of our business flyer to fit in with our new branding style and logo colour scheme. Wanting something with a bit of designer flair that I could not create myself. I have included the flyer which I created which lacks style so dazzle me.

I want to use the same content.

Text for main body of flyer is

Are you a small business owner, tradie or PAVC Service Provider struggling to stay on top of your bookkeeping and compliance obligations? If so we would love to help you get back on track and take control of your business finances so that you can make informed business decisions and focus on what you do best.

We have over 20 years industry experience and, as a small business ourselves, we are able to offer our clients a personal bookkeeping solution tailored to meet the needs of your business.

Accounts Payable | Accounts Receivable
Customer Invoicing
Bank and Credit Card Reconciliations
Payroll | Superannuation | Payroll Tax
Business Activity | Instalment Activity Statements
Regular Financial Reports
Ledgerly and BookPilot Set-Up and Training

```html
<!DOCTYPE html>
<html lang="en">
<head>
<meta charset="utf-8">
<title>Even Ledger Bookkeeping – A5 Flyer</title>
<link href="https://fonts.googleapis.com/css2?family=Exo+2:wght@500;600;700&family=Roboto+Condensed:wght@300;400&family=Roboto:wght@300&display=swap" rel="stylesheet">
<style>
  :root{
    --bg:#2b2b2b;
    --teal:#1fa7a0;
    --teal-deep:#0f6d7d;
    --navy:#0d4a63;
    --ink:#4a4a4a;
    --ink-soft:#5c5c5c;
    --paper:#ffffff;
    --mist:#e6e8ea;
    --silver:#c9cacc;
  }
  *{box-sizing:border-box;margin:0;padding:0}
  html,body{width:1054px;height:1200px;overflow:hidden;background:var(--bg)}
  .flyer{position:absolute;left:113px;top:21px;width:827px;height:1158px;background:var(--paper);overflow:hidden;font-family:"Exo 2",sans-serif}
  .hero-photo{position:absolute;left:0;top:0;width:827px;height:384px;
    background:linear-gradient(120deg,#c9d4dc 0%,#e9eef2 35%,#f4efe9 60%,#dfe7ee 100%)}
  .brand{position:absolute;right:28px;top:130px;display:flex;align-items:center;gap:12px}
  .brand-square{width:26px;height:26px;background:var(--teal)}
  .brand-name{font-family:"Roboto",sans-serif;font-weight:300;font-size:34px;letter-spacing:-.5px;color:var(--teal-deep)}
  .headline{position:absolute;left:0;top:384px;width:827px;height:164px;
    background:linear-gradient(100deg,var(--teal) 0%,var(--teal) 20%,var(--teal-deep) 60%,#2f6f80 100%);
    color:#fff;padding:20px 0 0 46px}
  .headline h1{font-weight:700;font-size:51px;letter-spacing:.5px;line-height:64px}
  .headline .sub{font-weight:600;font-size:52px;line-height:64px}
  .intro{position:absolute;left:0;top:548px;width:827px;height:151px;padding:16px 30px 0 46px;
    background:linear-gradient(180deg,#fff,#f1f2f3);font-weight:600;font-size:18px;line-height:23.5px;letter-spacing:.3px;color:var(--ink-soft)}
  .intro .lead{color:var(--teal-deep)}
  .offer{position:absolute;left:0;top:699px;width:414px;height:205px;padding:14px 30px 0 46px;
    background:linear-gradient(110deg,var(--navy) 0%,var(--teal-deep) 40%,var(--teal) 100%);
    color:#fff;font-weight:600;font-size:18px;line-height:29px;letter-spacing:.2px}
  .services{position:absolute;left:414px;top:699px;width:413px;height:205px;padding:14px 0 0 12px;
    background:linear-gradient(180deg,#eceef0,#dfe1e4);list-style:none;
    font-family:"Roboto Condensed",sans-serif;font-weight:300;font-size:16.5px;line-height:25.4px;color:var(--ink)}
  .services li{position:relative;padding-left:33px}
  .services li::before{content:"";position:absolute;left:2px;top:9px;width:8px;height:8px;background:var(--teal-deep)}
  .partners{position:absolute;left:0;top:904px;width:827px;height:98px;background:#fff;display:flex;align-items:center;
    font-weight:600;font-size:19px;letter-spacing:.4px;color:var(--ink-soft)}
  .partner{display:flex;align-items:center;gap:16px;position:absolute}
  .partner.ledgerly{left:61px}
  .partner.bookpilot{left:412px}
  .partner-dot{width:58px;height:58px;border-radius:50%;background:#17b3e4}
  .partner-badge{width:42px;height:56px;background:linear-gradient(180deg,#eef0ee 70%,#3ea34a 70%)}
  .agent{position:absolute;left:0;top:1002px;width:176px;height:156px;background:var(--silver);
    font-family:"Roboto Condensed",sans-serif;font-size:15.5px;line-height:25px;color:#333;padding-left:53px}
  .agent-seal{position:absolute;left:58px;top:18px;width:60px;height:60px;border-radius:50%;background:#f2f2f2;border:2px solid #888}
  .agent-seal::after{content:"";position:absolute;left:15px;top:15px;width:26px;height:26px;border-radius:50%;background:#b7c733}
  .agent-text{position:absolute;left:53px;top:95px}
  .contact{position:absolute;left:176px;top:1002px;width:651px;height:156px;
    background:linear-gradient(90deg,var(--teal) 0%,#2aa6a2 40%,#3a7f92 100%);color:#fff}
  .phone,.web{position:absolute;left:64px;display:flex;align-items:center}
  .phone{top:18px}
  .phone .num{margin-left:30px;font-weight:700;font-size:62px;letter-spacing:1px}
  .web{top:104px}
  .web .url{margin-left:30px;font-weight:600;font-size:19px;letter-spacing:.3px}
</style>
</head>
<body>
<main class="flyer">
  <div class="hero-photo" role="img" aria-label="Photo of a hand with a pen reviewing financial charts beside a calculator and laptop"></div>
  <div class="brand"><span class="brand-square"></span><span class="brand-name">EVEN LEDGER BOOKKEEPING</span></div>

  <header class="headline">
    <h1>BOOKKEEPING TAILORED</h1>
    <p class="sub">to your business needs</p>
  </header>

  <section class="intro">
    <p><span class="lead">Are you a small business owner, tradie or PAVC Service Provider struggling to stay on top of your bookkeeping and compliance obligations?</span> If so we would love to help you get back on track and take control of your business finances so that you can make informed business decisions and focus on what you do best.</p>
  </section>

  <section class="offer">
    <p>We have over 20 years industry experience and, as a small business ourselves, we are able to offer our clients a personal bookkeeping solution tailored to meet the needs of your business.</p>
  </section>

  <ul class="services">
    <li>Accounts Payable | Accounts Receivable</li>
    <li>Customer Invoicing</li>
    <li>Bank and Credit Card Reconciliations</li>
    <li>Payroll | Superannuation | Payroll Tax</li>
    <li>Business Activity | Instalment Activity Statements</li>
    <li>Regular Financial Reports</li>
    <li>Ledgerly and BookPilot Set-Up and Training</li>
  </ul>

  <section class="partners">
    <div class="partner ledgerly"><span class="partner-dot"></span><span>Ledgerly Certified Advisor</span></div>
    <div class="partner bookpilot"><span class="partner-badge"></span><span>BookPilot Pro Advisor</span></div>
  </section>

  <aside class="agent">
    <span class="agent-seal"></span>
    <p class="agent-text">BAS agent<br>20481937</p>
  </aside>

  <footer class="contact">
    <div class="phone">
      <svg width="30" height="30" viewBox="0 0 24 24" aria-hidden="true"><path fill="#fff" d="M6.6 10.8c1.4 2.8 3.8 5.1 6.6 6.6l2.2-2.2c.3-.3.7-.4 1-.2 1.1.4 2.3.6 3.6.6.6 0 1 .4 1 1V20c0 .6-.4 1-1 1C10.6 21 3 13.4 3 4c0-.6.4-1 1-1h3.5c.6 0 1 .4 1 1 0 1.3.2 2.5.6 3.6.1.3 0 .7-.2 1z"/></svg>
      <span class="num">0400 183 562</span>
    </div>
    <div class="web">
      <svg width="30" height="30" viewBox="0 0 24 24" aria-hidden="true" fill="none" stroke="#fff" stroke-width="1.5"><circle cx="12" cy="12" r="10"/><ellipse cx="12" cy="12" rx="4.5" ry="10"/><path d="M2 12h20M4 6.5h16M4 17.5h16"/></svg>
      <span class="url">www.evenledgerbookkeeping.com.au</span>
    </div>
  </footer>
</main>
</body>
</html>
```